Boutique Film/TV Company needs Business Card Design

Please see our website for background on our company and look of our current logo: www.lumarocpictures.ca

Pantone 314U is our main colour.

Target Market(s)

Network of peers, funders and broadcasters.

Industry/Entity Type

Business

Requirements
Must have
• We would like rounded corners and the height of the card to be shorter than traditional (maybe?!)

It's important that we have room for our office address, office number, cell number, email address, website, facebook and linked-in info (though not all of us have a linked-in account).

Would like the logo to keep the exclamation marks over the letters but the tag line/tag words of "film - television - interactive" can stay or go or... surprise me!

Nice to have
• Silky matte finish.

We are open to a change in the font of our logo/name.

```html
<!DOCTYPE html>
<html lang="en">
<head>
<meta charset="utf-8">
<title>Lumaroc Business Card</title>
<link rel="stylesheet" href="https://fonts.googleapis.com/css2?family=Marcellus&family=Fira+Sans:wght@400;500;600&display=swap">
<style>
  :root {
    --teal: #1a7f9b;
    --teal-dark: #0f6a85;
    --teal-light: #5aaec4;
    --ink: #231f20;
    --paper: #ffffff;
    --paper-shade: #e4e4e4;
    --stage: #d9d9d9;
    --muted: #3a3a3a;
  }
  * { box-sizing: border-box; margin: 0; padding: 0; }
  html, body { width: 1200px; height: 900px; overflow: hidden; }
  body {
    background: var(--stage);
    font-family: "Fira Sans", sans-serif;
    position: relative;
  }
  .card {
    position: absolute;
    top: 305px;
    width: 480px;
    height: 290px;
    border-radius: 18px;
    overflow: hidden;
    box-shadow: 0 8px 22px rgba(0,0,0,.18);
  }
  /* Front */
  .card-front {
    left: 90px;
    background: linear-gradient(200deg, var(--teal-light) 0%, var(--teal) 45%, var(--teal-dark) 100%);
  }
  .card-front .bubble { position: absolute; left: 0; top: 0; }
  .card-front .wordmark {
    position: absolute;
    left: 95px;
    top: 72px;
    font-family: "Marcellus", serif;
    font-size: 74px;
    color: var(--ink);
    line-height: 1;
  }
  .card-front .tagline {
    position: absolute;
    right: 26px;
    top: 196px;
    font-size: 20px;
    font-weight: 600;
    color: var(--paper);
    letter-spacing: .2px;
  }
  .card-front .website {
    position: absolute;
    right: 26px;
    bottom: 30px;
    font-size: 12px;
    color: var(--paper);
  }
  /* Back */
  .card-back {
    left: 630px;
    background: linear-gradient(215deg, var(--paper) 0%, var(--paper) 45%, var(--paper-shade) 100%);
  }
  .card-back .wordmark {
    position: absolute;
    left: 48px;
    top: 52px;
    font-family: "Marcellus", serif;
    font-size: 50px;
    color: var(--ink);
    line-height: 1;
  }
  .card-back .tagline {
    position: absolute;
    left: 50px;
    top: 120px;
    font-size: 13px;
    font-weight: 600;
    color: var(--teal);
  }
  .identity { position: absolute; left: 262px; top: 142px; }
  .identity .name { font-size: 20px; font-weight: 600; color: var(--teal); line-height: 1.1; }
  .identity .position { font-size: 12px; font-weight: 500; color: var(--ink); }
  .contacts {
    position: absolute;
    left: 266px;
    top: 192px;
    list-style: none;
    font-size: 8px;
    color: var(--muted);
    line-height: 11px;
  }
  .contacts li { display: flex; align-items: center; gap: 6px; }
  .contacts li.gap { margin-top: 6px; }
  .contacts .mark {
    width: 7px; height: 7px;
    background: var(--teal);
    border-radius: 1px;
    flex: none;
  }
</style>
</head>
<body>

<section class="card card-front" aria-label="Card front">
  <svg class="bubble" width="480" height="290" viewBox="0 0 480 290" aria-hidden="true">
    <path d="M66 58 H480 V176 H150 L172 210 L118 176 H66 Q50 176 50 160 V74 Q50 58 66 58 Z" fill="#ffffff"/>
  </svg>
  <div class="wordmark">Lumaroc</div>
  <div class="tagline">Films • Television • Interactive</div>
  <div class="website">www.lumarocpictures.ca</div>
</section>

<section class="card card-back" aria-label="Card back">
  <div class="wordmark">Lumaroc</div>
  <div class="tagline">Films • Television • Interactive</div>
  <div class="identity">
    <div class="name">Name Surname</div>
    <div class="position">Position</div>
  </div>
  <ul class="contacts">
    <li><span class="mark"></span>#123 Lorem Street, Dolor sit City, PA 19017</li>
    <li><span class="mark"></span>555.014.2870</li>
    <li class="gap"><span class="mark"></span>555.019.4412</li>
    <li><span class="mark"></span>name@lumarocpictures.com</li>
    <li><span class="mark"></span>lumarocpictures.facebook</li>
    <li><span class="mark"></span>lumarocpictures.linked-in</li>
    <li class="gap"><span class="mark"></span>www.lumarocpictures.ca</li>
  </ul>
</section>

</body>
</html>
```